" EMPRESA JOVEM INICIAMOS AS ATIVIDADES EM JULHO E ESTAMOS LANÇANDO 3 LINHAS DE COSMÉTICOS QUE INCLUEM: SABONETE LÍQUIDO, SHAMPOO, CONDICIONADOR, MÁSCARA CAPILAR, CREME PARA PENTEAR,HIDRATANTES, CREMES, ÁLCOOL GEL, FILTRO SOLAR, SHAMPOO MATIZADOR, AROMATIZADOR DE AMBIENTES ETC... "

```html
<!DOCTYPE html>
<html lang="pt-BR">
<head>
<meta charset="UTF-8">
<title>LUMERA – Shampoo e Condicionador Liso Brilhante</title>
<link href="https://fonts.googleapis.com/css2?family=Arimo:wght@400;500&display=swap" rel="stylesheet">
<style>
  :root{
    --page:#f4f3f1;
    --backdrop:#d9d4cd;
    --backdrop-light:#e6e2dc;
    --frame:#c9c3bb;
    --cap:#121110;
    --bottle:#ebe7e0;
    --bottle-edge:#cfc9c0;
    --gold-dark:#a97c45;
    --gold:#c99b5f;
    --gold-light:#e6c48e;
    --ink:#3a2c1c;
    --ink-soft:#5b4630;
    --logo:#f6ead2;
    --teal:#4fa9a3;
    --coral:#e58a7c;
    --cream:#f3e3c2;
    --mustard:#d9a64a;
    --label-white:#f7f4ee;
  }
  html,body{margin:0;padding:0;width:1200px;height:1200px;overflow:hidden;background:var(--page);}
  .canvas{position:relative;width:1200px;height:1200px;font-family:"Arimo",Arial,sans-serif;}
  .backdrop{position:absolute;left:60px;top:96px;width:1092px;height:1032px;
    background:radial-gradient(ellipse at 50% 45%,var(--backdrop-light),var(--backdrop));
    border:2px solid var(--frame);}
  .bottle,.cap,.pattern,.gold-band,.logo-box,.size-box{position:absolute;}
  .cap{background:linear-gradient(90deg,#000,#2a2826 45%,#000);}
  .bottle{background:linear-gradient(90deg,var(--bottle-edge),var(--bottle) 20%,#f8f6f2 50%,var(--bottle) 80%,var(--bottle-edge));overflow:hidden;}
  .pattern{left:0;width:100%;
    background:linear-gradient(135deg,var(--cream) 0%,var(--teal) 22%,var(--mustard) 42%,var(--coral) 62%,var(--cream) 80%,var(--teal) 100%);
    opacity:.9;}
  .gold-band{left:0;width:100%;box-sizing:border-box;
    background:linear-gradient(90deg,var(--gold-dark),var(--gold-light) 50%,var(--gold-dark));
    text-align:center;color:var(--ink);
    display:flex;flex-direction:column;align-items:center;}
  .logo-box{background:linear-gradient(135deg,var(--gold-dark),var(--gold) 50%,var(--gold-dark));display:flex;align-items:center;justify-content:center;z-index:1;}
  .brand-name{font-family:"Arimo",Arial,sans-serif;font-weight:400;color:var(--logo);letter-spacing:4px;white-space:nowrap;}
  .product-name{margin:0;font-size:43px;font-weight:400;line-height:1;}
  .product-claim{margin:6px 0 0;font-size:19px;line-height:1.2;color:var(--ink-soft);}
  .product-line{margin:16px 0 0;font-size:24px;line-height:1.2;color:var(--ink-soft);}
  .size-box{background:var(--label-white);text-align:center;color:var(--ink);}
  .size-box .salt{display:block;font-size:15px;margin-top:8px;}
  .size-box .volume{display:block;font-size:34px;line-height:1.05;}

  /* shampoo */
  .shampoo .cap{left:186px;top:168px;width:300px;height:100px;border-radius:8px 8px 2px 2px;}
  .shampoo .bottle{left:150px;top:252px;width:372px;height:866px;border-radius:34px 34px 26px 26px;}
  .shampoo .pattern.top{top:24px;height:252px;}
  .shampoo .logo-box{left:72px;top:48px;width:228px;height:214px;}
  .shampoo .brand-name{font-size:44px;}
  .shampoo .gold-band{top:276px;height:258px;justify-content:flex-end;padding-bottom:22px;}
  .shampoo .pattern.bottom{top:534px;height:240px;}
  .shampoo .size-box{left:96px;top:690px;width:180px;height:100px;}

  /* condicionador */
  .conditioner .bottle{left:606px;top:96px;width:468px;height:880px;border-radius:110px 110px 14px 14px / 50px 50px 14px 14px;}
  .conditioner .cap{left:630px;top:960px;width:420px;height:156px;border-radius:4px 4px 22px 22px;}
  .conditioner .pattern.top{top:24px;height:166px;}
  .conditioner .logo-box{left:129px;top:40px;width:210px;height:150px;}
  .conditioner .brand-name{font-size:40px;}
  .conditioner .gold-band{top:190px;height:146px;justify-content:center;}
  .conditioner .pattern.bottom{top:336px;height:364px;}
  .conditioner .size-box{left:144px;top:600px;width:180px;height:100px;}
</style>
</head>
<body>
<div class="canvas">
  <div class="backdrop"></div>

  <section class="product shampoo">
    <div class="cap"></div>
    <div class="bottle">
      <div class="pattern top" role="img" aria-label="Padrão geométrico de losangos coloridos em dourado, turquesa, coral e creme"></div>
      <div class="logo-box"><span class="brand-name">LUMERA</span></div>
      <div class="gold-band">
        <h2 class="product-name">Shampoo</h2>
        <p class="product-claim">proteção térmica anti frizz</p>
        <p class="product-line">Liso Brilhante</p>
      </div>
      <div class="pattern bottom" role="img" aria-label="Padrão geométrico de losangos coloridos em dourado, turquesa, coral e creme"></div>
      <div class="size-box"><span class="salt">Sem Sal</span><span class="volume">250ml</span></div>
    </div>
  </section>

  <section class="product conditioner">
    <div class="bottle">
      <div class="pattern top" role="img" aria-label="Padrão geométrico de losangos coloridos em dourado, turquesa, coral e creme"></div>
      <div class="logo-box"><span class="brand-name">LUMERA</span></div>
      <div class="gold-band">
        <h2 class="product-name">Condicionador</h2>
        <p class="product-claim">proteção térmica anti frizz</p>
        <p class="product-line">Liso Brilhante</p>
      </div>
      <div class="pattern bottom" role="img" aria-label="Padrão geométrico de losangos coloridos em dourado, turquesa, coral e creme"></div>
      <div class="size-box"><span class="salt">Sem Sal</span><span class="volume">250ml</span></div>
    </div>
    <div class="cap"></div>
  </section>
</div>
</body>
</html>
```